Premier nutraceutical company needs a label design.

We need a label design for a new product we're launching called Golden Meadow. Our company name, Vorabest, will be at the top of the label. I'll upload relevant files of different looks that I like.

```html
<!DOCTYPE html>
<html lang="en">
<head>
<meta charset="utf-8">
<title>Vorabest Golden Meadow Label</title>
<link rel="stylesheet" href="https://fonts.googleapis.com/css2?family=PT+Sans:wght@700&family=Oswald:wght@300;500&family=Roboto+Condensed:wght@400;500&display=swap">
<style>
  :root {
    --canvas: #f1f1f1;
    --green-deep: #0b5a26;
    --green-mid: #12853a;
    --green-light: #3fb152;
    --lime: #c9dc48;
    --lime-pale: #e4ec9a;
    --lime-band: #d6e52c;
    --white: #ffffff;
    --ink: #1d1d1b;
    --name-light: #eef1ea;
    --badge-ink: #1a2a12;
  }
  * { box-sizing: border-box; margin: 0; padding: 0; }
  html, body { width: 1200px; height: 1200px; overflow: hidden; background: var(--canvas); }
  .canvas { position: relative; width: 1200px; height: 1200px; }
  .label {
    position: absolute; left: 190px; top: 120px;
    width: 820px; height: 960px; overflow: hidden;
    background: var(--green-mid);
  }
  .label-art { position: absolute; inset: 0; width: 820px; height: 960px; }
  .brand {
    position: absolute; left: 0; right: 0; top: 118px;
    text-align: center;
    font-family: "PT Sans", sans-serif; font-weight: 700;
    font-size: 128px; letter-spacing: 14px; line-height: 1;
    color: var(--ink);
  }
  .product-name {
    position: absolute; left: 0; right: 0; top: 338px;
    text-align: center; color: var(--name-light);
    font-family: "Oswald", sans-serif; font-weight: 500; line-height: 1;
  }
  .product-name .line-1 { display: block; font-size: 112px; line-height: 112px; letter-spacing: 2px; }
  .product-name .line-2 { display: block; font-size: 84px; line-height: 84px; margin-top: 6px; letter-spacing: 1px; }
  .claim {
    position: absolute; left: 0; right: 0; top: 590px;
    text-align: center; color: var(--ink);
    font-family: "Roboto Condensed", sans-serif; font-weight: 400;
    font-size: 40px; line-height: 41px;
  }
  .count-badge {
    position: absolute; left: 0; right: 0; top: 787px;
    display: flex; align-items: center; justify-content: center;
  }
  .count-badge .count {
    width: 108px; height: 108px; border-radius: 50%;
    background: var(--lime-band); border: 6px solid var(--lime-pale);
    display: flex; align-items: center; justify-content: center;
    font-family: "Oswald", sans-serif; font-weight: 500; font-size: 66px;
    color: var(--badge-ink); position: relative; z-index: 1;
  }
  .count-badge .format {
    margin-left: -20px; height: 50px; padding: 0 22px 0 40px;
    border-radius: 25px; background: var(--lime-band);
    display: flex; align-items: center;
    font-family: "Oswald", sans-serif; font-weight: 500;
    font-size: 30px; color: var(--badge-ink); letter-spacing: 0.5px;
  }
  .supplement-type {
    position: absolute; left: 0; right: 0; top: 900px;
    text-align: center; color: var(--name-light);
    font-family: "Oswald", sans-serif; font-weight: 300; font-size: 30px; letter-spacing: 0.5px;
  }
</style>
</head>
<body>
<main class="canvas">
  <section class="label">
    <svg class="label-art" viewBox="0 0 820 960" xmlns="http://www.w3.org/2000/svg">
      <defs>
        <radialGradient id="panelGlow" cx="0.35" cy="0.35" r="0.8">
          <stop offset="0" stop-color="#4cbc5a"/>
          <stop offset="0.55" stop-color="#178c3c"/>
          <stop offset="1" stop-color="#0c6a2c"/>
        </radialGradient>
        <linearGradient id="bandFade" x1="0" x2="1" y1="0" y2="0">
          <stop offset="0" stop-color="#d6e52c" stop-opacity="0.55"/>
          <stop offset="0.35" stop-color="#d9e63a"/>
          <stop offset="0.7" stop-color="#d9e63a"/>
          <stop offset="1" stop-color="#c7d83a" stop-opacity="0.25"/>
        </linearGradient>
        <linearGradient id="groundTone" x1="0" x2="0" y1="0" y2="1">
          <stop offset="0" stop-color="#116b2e"/>
          <stop offset="1" stop-color="#0a4f22"/>
        </linearGradient>
        <linearGradient id="topWhite" x1="0" x2="0" y1="0" y2="1">
          <stop offset="0" stop-color="#ffffff"/>
          <stop offset="1" stop-color="#efefed"/>
        </linearGradient>
      </defs>
      <rect width="820" height="960" fill="url(#panelGlow)"/>
      <rect x="0" y="770" width="820" height="190" fill="url(#groundTone)" role="img" aria-label="Dark green grass blades pattern"/>
      <rect x="0" y="565" width="820" height="205" fill="url(#bandFade)"/>
      <path d="M0,0 H700 C760,90 800,250 740,300 C690,340 600,320 500,312 C380,300 230,305 150,330 C80,352 30,400 0,460 Z" fill="url(#topWhite)"/>
      <path d="M700,0 C760,90 800,250 740,300 C690,340 600,320 500,312" fill="none" stroke="var(--lime)" stroke-width="16"/>
      <path d="M150,330 C60,370 20,470 20,560 C20,700 50,860 110,960" fill="none" stroke="var(--lime)" stroke-width="18"/>
      <path d="M120,348 C35,400 -5,500 -5,580 C-5,720 25,870 80,960" fill="none" stroke="var(--lime-pale)" stroke-width="12"/>
      <path d="M95,365 C15,425 -30,520 -30,600 C-30,740 0,880 50,960" fill="none" stroke="var(--lime)" stroke-width="12"/>
      <path d="M70,385 C-5,450 -55,540 -55,620 C-55,760 -25,890 20,960" fill="none" stroke="var(--lime-pale)" stroke-width="10"/>
    </svg>
    <div class="brand">Vorabest</div>
    <h1 class="product-name"><span class="line-1">GOLDEN</span><span class="line-2">MEADOW</span></h1>
    <p class="claim">Supports cellular health,<br>promotes energy and vitality<br>by improving overall wellness<br>and bodily function.</p>
    <div class="count-badge"><span class="count">60</span><span class="format">VEGETABLE CAPSULES</span></div>
    <p class="supplement-type">DIETARY SUPPLEMENT</p>
  </section>
</main>
</body>
</html>
```